Bramblefen steakhouse dl flyer

We need a simple dl flyer for our restaurant bramblefen steakhouse. (formerly tildas restaurant at bramblefen lodge, lantern crest mountain, BC Canada)
DL format. double sided. Front Could be the same as poster, back to have additional photos and info.

Perhaps a stock photo of a Plated steak, and people at a bar is also needed.

Target Market(s)

25 to 55 year old skiers, couples, families

Industry/Entity Type

Restaurant

Requirements
Must have
• must tie in with the Bramblefen steakhouse poster.
Nice to have
• warm tones that tie in with the black poster, and flame grilled steak.
Should not have
• bright colours

```html
<!DOCTYPE html>
<html lang="en">
<head>
<meta charset="utf-8">
<title>Bramblefen Steakhouse DL Flyer</title>
<link rel="stylesheet" href="https://fonts.googleapis.com/css2?family=Marcellus&family=Tinos:wght@400;700&display=swap">
<style>
  :root {
    --page: #e9e6e1;
    --ink-dark: #1c1c1c;
    --ink-mid: #3a3a3a;
    --ink-soft: #4a4a4a;
    --paper: #f4f4f4;
    --text-light: #f1f1f1;
    --text-muted: #cfcfcf;
    --rule: #d8d8d8;
    --steak-deep: #5a2418;
    --steak-warm: #9b3b2a;
    --plate-warm: #b8743e;
    --plate-cream: #e8dccb;
  }
  * { box-sizing: border-box; margin: 0; padding: 0; }
  html, body { width: 1200px; height: 844px; overflow: hidden; }
  body {
    background: var(--page);
    position: relative;
    font-family: "Tinos", "Times New Roman", serif;
  }
  .flyer {
    position: absolute;
    top: 42px;
    width: 362px;
    height: 760px;
    overflow: hidden;
    box-shadow: 0 6px 18px rgba(0,0,0,.25);
  }
  .flyer--front {
    left: 200px;
    background: radial-gradient(ellipse at 60% 25%, var(--ink-soft) 0%, var(--ink-mid) 35%, var(--ink-dark) 100%);
  }
  .flyer--back {
    left: 638px;
    background: linear-gradient(160deg, var(--ink-soft) 0%, var(--ink-mid) 40%, var(--ink-dark) 100%);
  }

  .wordmark {
    font-family: "Marcellus", "Times New Roman", serif;
    color: var(--text-light);
    text-align: center;
    text-transform: uppercase;
    font-weight: 400;
    line-height: 0.95;
    letter-spacing: 1px;
  }
  .wordmark__rule { display: block; height: 1px; background: var(--rule); margin: 0 auto 4px; }

  /* Front */
  .front-brand { position: absolute; top: 42px; left: 0; right: 0; }
  .front-brand .wordmark__rule { width: 220px; }
  .front-brand .wordmark { font-size: 32px; }

  .photo { position: absolute; border-radius: 50%; }
  .photo--steak {
    left: 56px; top: 200px; width: 250px; height: 250px;
    background: radial-gradient(circle at 45% 55%, var(--steak-warm) 0%, var(--steak-deep) 55%, #2a1410 100%);
    box-shadow: 0 0 0 7px rgba(240,240,240,.85);
  }
  .photo--garnish-top {
    left: 70px; top: 148px; width: 104px; height: 90px;
    background: radial-gradient(circle, #6c5a2c 0%, #3a2a1a 60%, #d9d4cc 100%);
  }
  .photo--garnish-bottom {
    left: 222px; top: 410px; width: 112px; height: 90px;
    background: radial-gradient(circle, var(--plate-warm) 0%, #6a3a22 45%, var(--plate-cream) 100%);
  }

  .front-title { position: absolute; top: 560px; left: 0; right: 0; }
  .front-title .the {
    font-family: "Marcellus", serif;
    color: var(--text-light);
    text-align: center;
    font-size: 24px;
    letter-spacing: 2px;
  }
  .front-title .wordmark__rule { width: 290px; margin-top: 2px; }
  .front-title .wordmark { font-size: 40px; }
  .front-web {
    position: absolute; top: 692px; left: 0; right: 0;
    text-align: center; color: var(--text-muted);
    font-size: 11px; letter-spacing: 3px;
  }

  /* Back */
  .back-top {
    position: absolute; top: 0; left: 0; width: 362px; height: 290px;
  }
  .back-top svg { position: absolute; inset: 0; }
  .back-brand { position: absolute; top: 54px; left: 0; right: 0; }
  .back-brand .wordmark { color: var(--ink-mid); font-size: 20px; }
  .back-brand .wordmark__rule { width: 140px; background: var(--ink-mid); }
  .back-intro {
    position: absolute; top: 108px; left: 22px; right: 22px;
    color: var(--ink-mid); font-size: 13px; line-height: 1.15; text-align: center;
  }
  .back-intro p + p { margin-top: 10px; }

  .info { position: absolute; left: 0; right: 0; text-align: center; color: var(--text-light); }
  .info__icon { display: block; margin: 0 auto 4px; }
  .info__label { font-size: 11px; color: var(--text-muted); }
  .info__strong { font-weight: 700; font-size: 14px; line-height: 1.15; }
  .info__small { font-size: 11px; color: var(--text-muted); line-height: 1.2; }
  .info--location { top: 300px; }
  .info--reservations { top: 388px; }
  .info--hours { top: 502px; }

  .photo--plate {
    position: absolute; left: 0; bottom: 0; width: 362px; height: 145px;
    background: linear-gradient(180deg, #3b2a22 0%, var(--plate-warm) 45%, var(--plate-cream) 75%, #efe9e0 100%);
    clip-path: path("M0 40 Q181 -10 362 40 L362 145 L0 145 Z");
  }
</style>
</head>
<body>

  <section class="flyer flyer--front" aria-label="Flyer front">
    <header class="front-brand">
      <span class="wordmark__rule"></span>
      <h1 class="wordmark">Bramblefen<br>Steakhouse</h1>
    </header>

    <div class="photo photo--steak" role="img" aria-label="Photo of a flame grilled sliced steak"></div>
    <div class="photo photo--garnish-top" role="img" aria-label="Photo of a plated dish with herbs"></div>
    <div class="photo photo--garnish-bottom" role="img" aria-label="Photo of a plated steak with vegetables"></div>

    <div class="front-title">
      <p class="the">THE</p>
      <span class="wordmark__rule"></span>
      <h2 class="wordmark">Bramblefen<br>Steakhouse</h2>
    </div>
    <p class="front-web">www.bramblefensteak.com</p>
  </section>

  <section class="flyer flyer--back" aria-label="Flyer back">
    <div class="back-top">
      <svg width="362" height="290" viewBox="0 0 362 290" aria-hidden="true">
        <path d="M0 0 H362 V285 Q200 235 0 215 Z" fill="#f4f4f4"/>
      </svg>
      <div class="back-brand">
        <span class="wordmark__rule"></span>
        <h2 class="wordmark">Bramblefen<br>Steakhouse</h2>
      </div>
      <div class="back-intro">
        <p>The Bramblefen Steakhouse provides a casual, yet unparalleled mountain dining experience that is inspired by locally sourced food and wines from British Columbia.</p>
        <p>Here you can sample the best of Rocky Mountain Cuisine such as Elk, Bison,</p>
      </div>
    </div>

    <div class="info info--location">
      <svg class="info__icon" width="20" height="20" viewBox="0 0 20 20" aria-hidden="true">
        <circle cx="10" cy="10" r="10" fill="#f1f1f1"/>
        <path d="M5 10 L10 5.5 L15 10 H13.5 V14.5 H6.5 V10 Z" fill="#3a3a3a"/>
      </svg>
      <p class="info__label">We are conveniently located at</p>
      <p class="info__strong">Bramblefen Lodge<br>Lantern Crest Mountain Resort.</p>
    </div>

    <div class="info info--reservations">
      <svg class="info__icon" width="20" height="20" viewBox="0 0 20 20" aria-hidden="true">
        <circle cx="10" cy="10" r="10" fill="#f1f1f1"/>
        <path d="M5 8 Q10 4 15 8 L13.5 9.5 L12 8.5 H8 L6.5 9.5 Z M6.5 10.5 H13.5 L14.5 14 H5.5 Z" fill="#3a3a3a"/>
      </svg>
      <p class="info__label">For reservations call</p>
      <p class="info__strong">250-555-0148</p>
      <p class="info__small">and leave a message. Confirmation of reservation<br>call backs will be done between</p>
      <p class="info__strong">4pm - 5pm</p>
    </div>

    <div class="info info--hours">
      <svg class="info__icon" width="20" height="20" viewBox="0 0 20 20" aria-hidden="true">
        <circle cx="10" cy="10" r="10" fill="#f1f1f1"/>
        <circle cx="10" cy="10" r="5.5" fill="none" stroke="#3a3a3a" stroke-width="1.4"/>
        <path d="M10 7 V10 H12.5" fill="none" stroke="#3a3a3a" stroke-width="1.4"/>
      </svg>
      <p class="info__label">Opening Hours</p>
      <p class="info__strong">Dinner 5pm to 10pm.<br>Breakfast 7am to 10am</p>
      <p class="info__small">(Bookings essential for non-house guests)</p>
    </div>

    <div class="photo--plate" role="img" aria-label="Photo of a plated dish with red pepper and sauce"></div>
  </section>

</body>
</html>
```